Business Card needed for Drainor, a growing Septic Service company

Drainor, a growing local septic service company in Pennsylvania, needs updated business cards. We'd like the business card to feature our logo and communicate that we provide Septic Pumping, Installations/Repairs, Restroom Rentals, and 24/7 Emergency Service. The business card should be eye-catching, bold, and clean/simple. We have been in business almost 10 years and would like to expand and update our business brand and image.

Target Market(s)

Residential and Commercial, New and Current Homeowners

Industry/Entity Type

Service

Contact Information for Business Card

Contact on the business card should be: Dean Harlow Owner & Operator
Phone: 555-555-0187
Email: service@drainor-example.com
Website: www.drainor-example.com
Address: 812 Millbrook Lane Brookdale ST 00000

Font styles to use
Sans Serif

Colors

Designer to choose colors to be used in the design.

Requirements
Must have
• Feature logo on both side of business card.
Nice to have
• We envision the contact information on one side and our services listed on the other side. Utilize the green from the symbol in our logo as part of the design, overall design color scheme should be white, grey, black.

```html
<!DOCTYPE html>
<html lang="en">
<head>
<meta charset="utf-8">
<title>Drainor Business Card</title>
<link href="https://fonts.googleapis.com/css2?family=Barlow:wght@400;500;700&display=swap" rel="stylesheet">
<style>
  :root {
    --green: #8bbd22;
    --black: #1c1c1c;
    --deep: #0b0c0e;
    --white: #ffffff;
    --silver: #9c9fa3;
    --stage: #e6e6e4;
  }
  * { margin: 0; padding: 0; box-sizing: border-box; }
  html, body {
    width: 1200px; height: 800px; overflow: hidden;
    background: var(--stage);
    font-family: "Barlow", Arial, sans-serif;
  }
  .card {
    position: absolute;
    width: 560px; height: 320px;
    overflow: hidden;
    box-shadow: 0 6px 18px rgba(0,0,0,0.18);
  }
  .card-front { left: 60px; top: 60px; background: var(--white); }
  .card-back { left: 580px; top: 420px; background: var(--deep); }

  .band {
    position: absolute; left: 0; right: 0; bottom: 0; height: 64px;
    background: var(--green);
  }
  .band-edge {
    position: absolute; left: 0; right: 0; bottom: 64px; height: 8px;
    background: linear-gradient(90deg, #1a1a1a 0%, #3a3a3a 35%, #f4f4f4 50%, #3a3a3a 65%, #1a1a1a 100%);
  }

  .wordmark {
    position: absolute; display: flex; align-items: center; gap: 10px;
    font-weight: 700; text-transform: uppercase; letter-spacing: 1px; line-height: 1;
  }
  .wordmark-square { display: block; flex: none; }
  .card-front .wordmark { left: 30px; top: 78px; font-size: 40px; color: var(--black); }
  .card-front .wordmark-square { width: 32px; height: 32px; background: var(--green); }

  .website {
    position: absolute; left: 32px; top: 206px;
    font-size: 12px; letter-spacing: 3px; color: var(--green); font-weight: 500;
  }

  .contact { position: absolute; left: 318px; top: 52px; }
  .contact-name { font-size: 24px; font-weight: 500; color: var(--green); line-height: 1.1; }
  .contact-role { font-size: 18px; font-weight: 500; color: var(--black); margin-bottom: 20px; }
  .contact-line {
    display: flex; align-items: center; gap: 8px;
    font-size: 12px; color: var(--black); margin-bottom: 9px; white-space: nowrap;
  }
  .contact-line svg { width: 15px; height: 15px; flex: none; }

  .card-back .wordmark { left: 170px; top: 92px; font-size: 46px; color: var(--silver); }
  .card-back .wordmark-square { width: 36px; height: 36px; background: var(--silver); }
  .services {
    position: absolute; left: 0; right: 0; bottom: 0; height: 64px;
    display: flex; align-items: center; justify-content: space-between;
    padding: 0 22px; list-style: none;
    color: var(--white); font-size: 14px; font-weight: 500; white-space: nowrap;
  }
</style>
</head>
<body>
  <section class="card card-front" aria-label="Business card front">
    <div class="wordmark"><span class="wordmark-square"></span>Drainor</div>
    <div class="website">www.drainor-example.com</div>

    <div class="contact">
      <p class="contact-name">Dean Harlow</p>
      <p class="contact-role">Owner &amp; Operator</p>
      <p class="contact-line">
        <svg viewBox="0 0 16 16" aria-hidden="true"><circle cx="8" cy="8" r="7" fill="none" stroke="var(--green)" stroke-width="1.3"/><path d="M5.5 4.5 L7 6 L6.2 7 Q7 8.8 9 9.8 L10 9 L11.5 10.5 L10.5 11.5 Q6 11 4.5 5.5 Z" fill="var(--green)"/></svg>
        555-555-0187
      </p>
      <p class="contact-line">
        <svg viewBox="0 0 16 16" aria-hidden="true"><circle cx="8" cy="8" r="7" fill="none" stroke="var(--green)" stroke-width="1.3"/><circle cx="8" cy="8" r="2.4" fill="none" stroke="var(--green)" stroke-width="1.3"/><path d="M10.4 6 V9.3 Q10.4 10.6 11.6 10.3" fill="none" stroke="var(--green)" stroke-width="1.3"/></svg>
        service@drainor-example.com
      </p>
      <p class="contact-line">
        <svg viewBox="0 0 16 16" aria-hidden="true"><path d="M8 15 C4 10 3 8 3 6 A5 5 0 0 1 13 6 C13 8 12 10 8 15 Z" fill="none" stroke="var(--green)" stroke-width="1.3"/><circle cx="8" cy="6" r="1.8" fill="var(--green)"/></svg>
        812 Millbrook Lane Brookdale ST 00000
      </p>
    </div>

    <div class="band-edge"></div>
    <div class="band"></div>
  </section>

  <section class="card card-back" aria-label="Business card back">
    <div class="wordmark"><span class="wordmark-square"></span>Drainor</div>
    <div class="band-edge"></div>
    <div class="band"></div>
    <ul class="services">
      <li>Septic Pumping</li>
      <li>Restroom Rentals</li>
      <li>Installations/Repairs</li>
      <li>24/7 Emergency Service</li>
    </ul>
  </section>
</body>
</html>
```